Business Card for Brevel Coatings

We need a simple, yet out standing business card for our painting company.

Target Market(s)

wealthy; high-end neighborhoods, and businesses

Industry/Entity Type

Painting

Contact Information for Business Card

Name:
Doran Vask

Email:
d.vask@brevel-coatings.com

Website:
Brevel-coatings.com

Phone Number:
(555) 416-9073

Font styles to use
Serif
Sans Serif

Requirements
Must have
• slogan "making change simple"
Should not have
• A title attached to the name on the card

```html
<!DOCTYPE html>
<html lang="en">
<head>
<meta charset="utf-8">
<title>Brevel Coatings – Business Card</title>
<link href="https://fonts.googleapis.com/css2?family=Cinzel:wght@500;600&family=Lato:wght@400;700&display=swap" rel="stylesheet">
<style>
  :root {
    --green-deep: #1f6b38;
    --green-mid: #2a7f45;
    --green-dark: #2f5a14;
    --lime: #8cc63f;
    --olive: #7fa33a;
    --white: #ffffff;
    --backdrop: #e9ebe8;
  }
  * { box-sizing: border-box; margin: 0; padding: 0; }
  html, body { width: 1200px; height: 898px; overflow: hidden; }
  body {
    background: var(--backdrop);
    font-family: "Lato", Arial, sans-serif;
    position: relative;
  }
  .card {
    position: absolute;
    width: 600px;
    height: 343px;
    box-shadow: 0 4px 14px rgba(0,0,0,0.18);
    overflow: hidden;
  }
  .brand { position: absolute; display: flex; align-items: center; gap: 14px; }
  .brand-dot { width: 20px; height: 20px; border-radius: 50%; background: var(--lime); flex: none; }
  .brand-name {
    font-family: "Cinzel", Georgia, serif;
    font-weight: 600; letter-spacing: 1px; line-height: 1;
  }
  .slogan {
    position: absolute;
    font-family: "Cinzel", Georgia, serif;
    font-weight: 500; font-size: 14px; letter-spacing: 6px; line-height: 1;
    color: var(--olive);
  }

  /* Front */
  .card-front {
    left: 300px; top: 62px;
    background: radial-gradient(ellipse at 40% 25%, var(--green-mid) 0%, var(--green-deep) 75%);
  }
  .card-front .brand { left: 0; right: 0; top: 122px; justify-content: center; }
  .card-front .brand-name { color: var(--white); font-size: 38px; }
  .card-front .slogan { left: 0; right: 0; top: 176px; text-align: center; color: var(--lime); }
  .front-web {
    position: absolute; left: 0; right: 0; bottom: 46px;
    text-align: center; color: var(--white); font-size: 15px; letter-spacing: 2px;
  }

  /* Back */
  .card-back { left: 300px; top: 474px; background: var(--white); }
  .back-shape { position: absolute; inset: 0; }
  .card-back .brand { left: 48px; top: 98px; }
  .card-back .brand-name { color: var(--green-dark); font-size: 33px; }
  .card-back .slogan { left: 82px; top: 146px; font-size: 12px; letter-spacing: 5px; }
  .holder-name {
    position: absolute; right: 52px; top: 166px;
    color: var(--white); font-size: 24px; font-weight: 400;
  }
  .contact-list { position: absolute; right: 40px; top: 208px; list-style: none; }
  .contact-list li {
    color: var(--white); font-size: 15px; line-height: 22px;
    display: flex; justify-content: flex-end; align-items: center; gap: 8px;
  }
  .contact-list svg { width: 13px; height: 13px; flex: none; }
  .address {
    position: absolute; left: 52px; bottom: 22px;
    color: var(--white); font-size: 16px; line-height: 21px;
  }
</style>
</head>
<body>

<section class="card card-front">
  <div class="brand">
    <span class="brand-dot"></span>
    <span class="brand-name">Brevel Coatings</span>
  </div>
  <p class="slogan">MAKING CHANGE SIMPLE</p>
  <p class="front-web">www.brevel-coatings.com</p>
</section>

<section class="card card-back">
  <svg class="back-shape" viewBox="0 0 600 343" preserveAspectRatio="none" aria-hidden="true">
    <defs>
      <linearGradient id="bandFill" x1="0" y1="1" x2="1" y2="0">
        <stop offset="0" stop-color="#1f6b38"/>
        <stop offset="1" stop-color="#2a7f45"/>
      </linearGradient>
    </defs>
    <path d="M0,262 C230,252 430,185 540,0 L600,0 L600,343 L0,343 Z" fill="url(#bandFill)"/>
    <path d="M330,222 C440,165 500,98 532,0 L552,0 C508,108 440,176 330,222 Z" fill="#8cc63f"/>
  </svg>

  <div class="brand">
    <span class="brand-dot"></span>
    <span class="brand-name">Brevel Coatings</span>
  </div>
  <p class="slogan">MAKING CHANGE SIMPLE</p>

  <p class="holder-name">Doran Vask</p>

  <ul class="contact-list">
    <li>(555) 416-9073
      <svg viewBox="0 0 16 16"><path d="M4 1l3 3-2 2c1 2 3 4 5 5l2-2 3 3-2 3C7 15 1 9 1 3z" fill="#8cc63f"/></svg>
    </li>
    <li>d.vask@brevel-coatings.com
      <svg viewBox="0 0 16 16"><rect x="1" y="3" width="14" height="10" fill="#8cc63f"/><path d="M1 3l7 6 7-6" fill="none" stroke="#1f6b38" stroke-width="1.5"/></svg>
    </li>
    <li>www.brevel-coatings.com
      <svg viewBox="0 0 16 16"><circle cx="8" cy="8" r="7" fill="#8cc63f"/><path d="M1 8h14M8 1v14M3 4h10M3 12h10" stroke="#1f6b38" stroke-width="1" fill="none"/></svg>
    </li>
  </ul>

  <p class="address">4418 Marlow Lane<br>Easton TX 75000</p>
</section>

</body>
</html>
```